Need Letterhead Design & Matching Business Card

I have a logo that I love already. But the letterhead is less than appealing and boring. I'd like a design for my letterhead which I will match with business cards. Also, I'd like to have used fonts that are generally available, as my current letterhead uses a font named "SPACE" which nobody has unless they download it...so when a Word version is forwarded, it looks awful on the receiver's screed due to not having the font. That being said, modern is the look we like and are going for.

My business is "Halloran Brightmoor PC" - a law firm specializing in representing people who have suffered catastrophic injuries or death (plane, auto, train crashes etc.).

See attached letterhead, which has all of the pertinent information. My logo is also attached in various formats.

```html
<!DOCTYPE html>
<html lang="en">
<head>
<meta charset="utf-8">
<title>Halloran Brightmoor PC — Stationery</title>
<link rel="stylesheet" href="https://fonts.googleapis.com/css2?family=Open+Sans:wght@700&display=swap">
<style>
  :root {
    --ink: #000000;
    --paper: #ffffff;
    --backdrop: #cfcfcf;
    --font-main: "Open Sans", Arial, sans-serif;
  }
  * { box-sizing: border-box; margin: 0; padding: 0; }
  html, body { width: 1200px; height: 1000px; overflow: hidden; }
  body { background: var(--backdrop); font-family: var(--font-main); font-weight: 700; position: relative; }

  .sheet { position: absolute; background: var(--paper); }
  .block { position: absolute; background: var(--ink); color: var(--paper); overflow: hidden; }

  .brand { position: absolute; display: flex; align-items: flex-start; }
  .brand__square { flex: none; }
  .brand__name { line-height: 1.13; white-space: nowrap; }
  .brand--dark .brand__square { background: var(--ink); }
  .brand--dark .brand__name { color: var(--ink); }
  .brand--light .brand__square { background: var(--paper); }
  .brand--light .brand__name { color: var(--paper); }

  .info { position: absolute; color: var(--paper); line-height: 1.35; white-space: nowrap; }
  .info__row { display: flex; align-items: center; gap: 3px; }
  .info__row svg { fill: var(--paper); flex: none; }

  /* Letterhead */
  .letterhead { left: 110px; top: 160px; width: 518px; height: 672px; }
  .letterhead .brand--top { left: 27px; top: 33px; }
  .letterhead .brand--top .brand__square { width: 53px; height: 55px; margin-right: 7px; }
  .letterhead .brand--top .brand__name { font-size: 16px; margin-top: 1px; }
  .letterhead .footer-logo { left: 13px; top: 553px; width: 156px; height: 105px; }
  .letterhead .footer-logo .brand { left: 24px; top: 30px; }
  .letterhead .footer-logo .brand__square { width: 42px; height: 42px; margin-right: 5px; }
  .letterhead .footer-logo .brand__name { font-size: 12.5px; line-height: 1.15; margin-top: -1px; }
  .letterhead .footer-contact { left: 174px; top: 601px; width: 169px; height: 57px; }
  .letterhead .footer-address { left: 347px; top: 601px; width: 156px; height: 57px; }
  .letterhead .info { font-size: 7.5px; left: 34px; top: 13px; }
  .letterhead .footer-address .info { left: 23px; }

  /* Business card — front */
  .card-front { left: 690px; top: 248px; width: 402px; height: 230px; background: var(--ink); }
  .card-front .brand { left: 103px; top: 72px; }
  .card-front .brand__square { width: 72px; height: 72px; margin-right: 9px; margin-top: 5px; }
  .card-front .brand__name { font-size: 24px; line-height: 1.12; }

  /* Business card — back */
  .card-back { left: 690px; top: 521px; width: 402px; height: 229px; }
  .card-back .brand--top { left: 197px; top: 64px; }
  .card-back .brand--top .brand__square { width: 53px; height: 53px; margin-right: 7px; }
  .card-back .brand--top .brand__name { font-size: 16px; }
  .card-back .footer-logo { left: 15px; top: 132px; width: 123px; height: 84px; }
  .card-back .footer-logo .brand { left: 10px; top: 22px; }
  .card-back .footer-logo .brand__square { width: 36px; height: 36px; margin-right: 5px; }
  .card-back .footer-logo .brand__name { font-size: 10.5px; line-height: 1.15; margin-top: 1px; }
  .card-back .footer-contact { left: 141px; top: 167px; width: 121px; height: 49px; }
  .card-back .footer-address { left: 265px; top: 167px; width: 123px; height: 49px; }
  .card-back .info { font-size: 5.6px; left: 24px; top: 12px; }
  .card-back .footer-address .info { left: 16px; }
</style>
</head>
<body>

<svg width="0" height="0" style="position:absolute" aria-hidden="true">
  <symbol id="icon-mail" viewBox="0 0 10 8"><rect x="0" y="0" width="10" height="8" rx="1"/></symbol>
  <symbol id="icon-web" viewBox="0 0 10 10"><circle cx="5" cy="5" r="5"/></symbol>
  <symbol id="icon-phone" viewBox="0 0 10 10"><path d="M2 0 L4 2.5 L3 4 Q4.5 6 6 7 L7.5 6 L10 8 L8.5 10 Q3 9.5 0 1.5 Z"/></symbol>
</svg>

<!-- Letterhead -->
<section class="sheet letterhead" aria-label="Letterhead">
  <div class="brand brand--dark brand--top">
    <span class="brand__square"></span>
    <span class="brand__name">Halloran<br>Brightmoor<br>PC</span>
  </div>

  <div class="block footer-logo">
    <div class="brand brand--light">
      <span class="brand__square"></span>
      <span class="brand__name">Halloran<br>Brightmoor<br>PC</span>
    </div>
  </div>
  <div class="block footer-contact">
    <div class="info">
      <div class="info__row"><svg width="8" height="6"><use href="#icon-mail"/></svg>miles@halloranbrightmoor.com</div>
      <div class="info__row"><svg width="7" height="7"><use href="#icon-web"/></svg>www.halloranbrightmoor.com</div>
      <div class="info__row"><svg width="7" height="7"><use href="#icon-phone"/></svg>Tel: (555) 014-2270</div>
    </div>
  </div>
  <div class="block footer-address">
    <div class="info">
      <div>R. Miles Ferrand, Esq. | President</div>
      <div>4120 Larkspur Ave. | suite 800</div>
      <div>Westbrook, CA 90000</div>
    </div>
  </div>
</section>

<!-- Business card front -->
<section class="sheet card-front" aria-label="Business card front">
  <div class="brand brand--light">
    <span class="brand__square"></span>
    <span class="brand__name">Halloran<br>Brightmoor<br>PC</span>
  </div>
</section>

<!-- Business card back -->
<section class="sheet card-back" aria-label="Business card back">
  <div class="brand brand--dark brand--top">
    <span class="brand__square"></span>
    <span class="brand__name">Halloran<br>Brightmoor<br>PC</span>
  </div>

  <div class="block footer-logo">
    <div class="brand brand--light">
      <span class="brand__square"></span>
      <span class="brand__name">Halloran<br>Brightmoor<br>PC</span>
    </div>
  </div>
  <div class="block footer-contact">
    <div class="info">
      <div class="info__row"><svg width="6" height="5"><use href="#icon-mail"/></svg>miles@halloranbrightmoor.com</div>
      <div class="info__row"><svg width="5" height="5"><use href="#icon-web"/></svg>www.halloranbrightmoor.com</div>
      <div class="info__row"><svg width="5" height="5"><use href="#icon-phone"/></svg>Tel: (555) 014-2270</div>
    </div>
  </div>
  <div class="block footer-address">
    <div class="info">
      <div>R. Miles Ferrand, Esq. | President</div>
      <div>4120 Larkspur Ave. | suite 800</div>
      <div>Westbrook, CA 90000</div>
    </div>
  </div>
</section>

</body>
</html>
```